Criação de Manual da Marca para Marketing & Comunicação
A empresa queria:
" Vamos iniciar atividade em junho. Incialmente, eugência com prestadores terceirizados, venda via network, em seguida tráfego pago e orgânico. Pretendo terceirizar a produção de criativos e vídeos. "

```html
<!DOCTYPE html>
<html lang="pt">
<head>
<meta charset="utf-8">
<title>Manual da Marca — Limites de redução e Proibições</title>
<link rel="stylesheet" href="https://fonts.googleapis.com/css2?family=Montserrat:wght@400;600;700&display=swap">
<style>
:root{
  --page:#ffffff;
  --sheet:#f3f3f3;
  --sheet-edge:#e6e6e6;
  --panel:#25282c;
  --ink:#2b2b2b;
  --muted:#8a8a8a;
  --light:#d9d9d9;
  --red:#d9413f;
  --accent:#1f8fc9;
}
*{margin:0;padding:0;box-sizing:border-box}
html,body{width:1200px;height:1200px;overflow:hidden;background:var(--page);font-family:"Montserrat",sans-serif;color:var(--ink)}
.spread{position:absolute;left:0;top:283px;width:1200px;height:634px;background:linear-gradient(90deg,var(--sheet) 0%,#fafafa 55%,var(--sheet) 100%);border-top:1px solid var(--sheet-edge);border-bottom:1px solid var(--sheet-edge)}
.side-panel{position:absolute;left:0;top:0;width:269px;height:634px;background:var(--panel);color:#fff}
.side-panel h2{position:absolute;left:38px;top:202px;font-size:15px;font-weight:700}
.side-panel p{position:absolute;left:38px;font-size:8.5px;line-height:14px;color:#d6d6d6;width:200px}
.side-panel .rule{top:226px}
.side-panel .size{top:270px}
.brand{position:absolute;left:36px;top:510px;display:flex;align-items:center;gap:10px}
.brand .mark{width:22px;height:22px;background:var(--accent)}
.brand span{font-size:26px;font-weight:700;letter-spacing:2px;color:#fff}
.reduction .sample{position:absolute;font-size:7px;font-weight:700;color:var(--ink);letter-spacing:.5px;border:1px solid var(--light);padding:3px 4px;background:#fff}
.reduction .tag{position:absolute;font-size:6px;color:var(--muted)}
.prohibitions .item{position:absolute;width:64px;text-align:center}
.item .label{font-size:5px;line-height:6px;color:var(--muted);height:14px;display:flex;align-items:flex-end;justify-content:center}
.item .thumb{position:relative;margin:3px auto 0;width:56px;height:34px;background:#fff;border:1px solid var(--light);display:flex;align-items:center;justify-content:center;font-size:7.5px;font-weight:700;letter-spacing:.5px;color:var(--ink)}
.item .thumb svg{position:absolute;inset:0;width:100%;height:100%}
.item .thumb.dark{background:#3a3030;color:#5a4a4a}
.intro{position:absolute;left:996px;top:204px;width:156px}
.intro h2{font-size:15px;font-weight:700;margin-bottom:8px}
.intro p{font-size:8px;line-height:12.5px;color:#555;margin-bottom:10px}
.intro strong{color:var(--ink)}
.folio{position:absolute;right:28px;bottom:30px;font-size:7px;font-weight:700;color:var(--ink)}
</style>
</head>
<body>
<section class="spread">
  <aside class="side-panel">
    <h2>Limites de redução</h2>
    <p class="rule">O logo deve ser sempre redimensionado respeitando as proporções originais.</p>
    <p class="size">25 mm ou 295 px na horizontal</p>
    <div class="brand"><div class="mark"></div><span>VERTEXA</span></div>
  </aside>

  <div class="reduction">
    <span class="tag" style="left:352px;top:287px">15 mm</span>
    <div class="sample" style="left:392px;top:281px">VERTEXA</div>
    <span class="tag" style="left:418px;top:318px">25 mm</span>
    <span class="tag" style="left:462px;top:287px">145 px</span>
    <div class="sample" style="left:500px;top:281px">VERTEXA</div>
    <span class="tag" style="left:520px;top:318px">295 px</span>
  </div>

  <div class="prohibitions">
    <div class="item" style="left:711px;top:325px"><div class="label">Distorcer proporções</div><div class="thumb">VERTEXA<svg viewBox="0 0 56 34" preserveAspectRatio="none"><path d="M4 2L52 32M52 2L4 32" stroke="#d9413f" stroke-width="1.5"/></svg></div></div>
    <div class="item" style="left:781px;top:325px"><div class="label">Alterar cores</div><div class="thumb">VERTEXA<svg viewBox="0 0 56 34" preserveAspectRatio="none"><path d="M4 2L52 32M52 2L4 32" stroke="#d9413f" stroke-width="1.5"/></svg></div></div>
    <div class="item" style="left:851px;top:325px"><div class="label">Rotacionar o logo</div><div class="thumb">VERTEXA<svg viewBox="0 0 56 34" preserveAspectRatio="none"><path d="M4 2L52 32M52 2L4 32" stroke="#d9413f" stroke-width="1.5"/></svg></div></div>
    <div class="item" style="left:921px;top:325px"><div class="label">Aplicar sobre fundo poluído</div><div class="thumb">VERTEXA<svg viewBox="0 0 56 34" preserveAspectRatio="none"><path d="M4 2L52 32M52 2L4 32" stroke="#d9413f" stroke-width="1.5"/></svg></div></div>

    <div class="item" style="left:711px;top:405px"><div class="label">Mudar tipografia</div><div class="thumb">VERTEXA<svg viewBox="0 0 56 34" preserveAspectRatio="none"><path d="M4 2L52 32M52 2L4 32" stroke="#d9413f" stroke-width="1.5"/></svg></div></div>
    <div class="item" style="left:781px;top:405px"><div class="label">Adicionar sombra</div><div class="thumb">VERTEXA<svg viewBox="0 0 56 34" preserveAspectRatio="none"><path d="M4 2L52 32M52 2L4 32" stroke="#d9413f" stroke-width="1.5"/></svg></div></div>
    <div class="item" style="left:851px;top:405px"><div class="label">Usar contorno</div><div class="thumb">VERTEXA<svg viewBox="0 0 56 34" preserveAspectRatio="none"><path d="M4 2L52 32M52 2L4 32" stroke="#d9413f" stroke-width="1.5"/></svg></div></div>
    <div class="item" style="left:921px;top:405px"><div class="label">Esticar</div><div class="thumb">VERTEXA<svg viewBox="0 0 56 34" preserveAspectRatio="none"><path d="M4 2L52 32M52 2L4 32" stroke="#d9413f" stroke-width="1.5"/></svg></div></div>

    <div class="item" style="left:711px;top:500px"><div class="label">Reorganizar elementos</div><div class="thumb">VERTEXA<svg viewBox="0 0 56 34" preserveAspectRatio="none"><path d="M4 2L52 32M52 2L4 32" stroke="#d9413f" stroke-width="1.5"/></svg></div></div>
    <div class="item" style="left:781px;top:500px"><div class="label">Aplicar em baixo contraste</div><div class="thumb">VERTEXA<svg viewBox="0 0 56 34" preserveAspectRatio="none"><path d="M4 2L52 32M52 2L4 32" stroke="#d9413f" stroke-width="1.5"/></svg></div></div>
    <div class="item" style="left:851px;top:500px"><div class="label">Fundo escuro sem versão</div><div class="thumb dark">VERTEXA</div></div>
  </div>

  <div class="intro">
    <h2>Proibições</h2>
    <p>Abaixo, estão alguns exemplos do que não fazer com a marca <strong>VERTEXA.</strong></p>
    <p>Quebrar as regras implica na má utilização e desfigura a marca. Alguns manuais não preveem aplicação adequada da marca para diversas situações. Por isso, muitas vezes a marca é utilizada de forma errada, desvalorizando a imagem da empresa.</p>
  </div>

  <span class="folio">08</span>
</section>
</body>
</html>
```